Single-sided business card for restaurant bellwether with new logo made on this site

Business card options with new logo including restaurant name, address, phone number and website. This business card is single-sided only and will be presented at the hostess desk for clients to take. I would like to see options based on a cream card background, a white card background, a yellow card background and a burgundy colored background. It needs to be elegant and traditional.

Target Market(s)

local and international crowd

Industry/Entity Type

restaurant

Contact Information for Business Card

address, website and phone number

Font styles to use
Serif

Colors
EE7325
F08F49
F5BC92
FAE3D3
FDF4ED

Requirements
Must have
• new logo, address, phone number, website
Should not have
• more than three colors

```html
<!DOCTYPE html>
<html lang="es">
<head>
<meta charset="utf-8">
<title>Restaurant Bellwether – tarjetas de presentación</title>
<link rel="stylesheet" href="https://fonts.googleapis.com/css2?family=Source+Sans+3:wght@400;500&display=swap">
<style>
  :root{
    --stage:#8f8f8f;
    --cream:#fdf8ec;
    --burgundy:#7a1014;
    --amber:#f9b13c;
    --ink:#3d1512;
    --white:#ffffff;
    --leaf-soft:#f7d6a8;
    --icon:#f3a73a;
  }
  *{margin:0;padding:0;box-sizing:border-box}
  html,body{width:703px;height:1200px;overflow:hidden;background:var(--stage)}
  body{position:relative;font-family:"Source Sans 3",sans-serif}
  .card{position:absolute;left:92px;width:504px;height:288px;overflow:hidden}
  .card--cream{top:104px;background:var(--cream);color:var(--ink)}
  .card--burgundy{top:454px;background:var(--burgundy);color:var(--white)}
  .card--amber{top:803px;background:var(--amber);color:var(--ink)}
  .frame{position:absolute;inset:0}
  .leaf{position:absolute;width:64px;height:64px;border-radius:50%;
        background:radial-gradient(circle,var(--leaf) 0%,var(--leaf) 35%,transparent 70%)}
  .card--cream{--leaf:var(--leaf-soft);--line:var(--ink)}
  .card--burgundy{--leaf:var(--leaf-soft);--line:var(--white)}
  .card--amber{--leaf:var(--white);--line:var(--white)}
  .leaf--top{left:222px;top:-32px}
  .leaf--bottom{left:222px;bottom:-32px}
  .leaf--left{left:-32px;top:110px}
  .leaf--right{right:-32px;top:106px}
  .brand{position:absolute;left:60px;top:116px;width:116px;text-align:center}
  .brand__mark{display:block;width:62px;height:58px;margin:0 auto 8px}
  .card--burgundy .brand__mark{background:var(--white)}
  .card--amber .brand__mark{background:var(--ink)}
  .brand__name{font-size:16px;font-weight:500;letter-spacing:2.5px;line-height:1}
  .card--burgundy .brand__name{color:var(--white)}
  .brand--boxed{left:50px;top:70px;width:104px;height:152px;background:var(--amber);
                display:flex;align-items:center;justify-content:center}
  .brand--boxed .brand__name{font-size:14px;letter-spacing:1.5px;color:var(--ink)}
  .title{position:absolute;left:231px;top:65px;font-size:23px;font-weight:400;letter-spacing:-.2px}
  .contact{position:absolute;left:239px;top:112px;list-style:none;font-size:13px;line-height:19.6px}
  .contact li{position:relative;padding-left:31px;margin-bottom:7px}
  .contact svg{position:absolute;left:0;top:2px;width:14px;height:15px;fill:none;stroke:var(--icon);stroke-width:1.3}
  .card--amber .contact svg{stroke:var(--white)}
</style>
</head>
<body>

<!-- Cream -->
<section class="card card--cream">
  <div class="leaf leaf--top" role="img" aria-label="Decoración de hojas de agave"></div>
  <div class="leaf leaf--bottom" role="img" aria-label="Decoración de hojas de agave"></div>
  <div class="leaf leaf--left" role="img" aria-label="Decoración de hojas de agave"></div>
  <div class="leaf leaf--right" role="img" aria-label="Decoración de hojas de agave"></div>
  <svg class="frame" viewBox="0 0 504 288" fill="none" stroke="var(--line)" stroke-width="0.8">
    <path d="M217 18H36Q14 18 14 40V110"/><path d="M14 175V248Q14 270 36 270H218"/>
    <path d="M291 270H464Q486 270 486 248V175"/><path d="M486 101V40Q486 18 464 18H296"/>
    <g fill="var(--line)" stroke="none">
      <circle cx="217" cy="18" r="2"/><circle cx="296" cy="18" r="2"/>
      <circle cx="218" cy="270" r="2"/><circle cx="291" cy="270" r="2"/>
      <circle cx="14" cy="110" r="2"/><circle cx="14" cy="175" r="2"/>
      <circle cx="486" cy="101" r="2"/><circle cx="486" cy="175" r="2"/>
    </g>
  </svg>
  <div class="brand brand--boxed"><span class="brand__name">BELLWETHER</span></div>
  <h1 class="title">Restaurant Bellwether</h1>
  <ul class="contact">
    <li><svg viewBox="0 0 14 15"><path d="M2 2l3 0 1 3-2 1c1 2 2 3 4 4l1-2 3 1 0 3c-6 0-10-4-10-10z"/></svg>Reservaciones 958-555-0142</li>
    <li><svg viewBox="0 0 14 15"><path d="M7 14C3 9 2 7 2 5a5 5 0 0110 0c0 2-1 4-5 9z"/><circle cx="7" cy="5" r="1.8"/></svg>Jacarandá 415<br>Bahía del Sol,<br>Oaxaca CP 70900</li>
    <li><svg viewBox="0 0 14 15"><path d="M3 1v11l3-3 2 5 2-1-2-5h4z"/></svg>www.bellwether.com.mx</li>
  </ul>
</section>

<!-- Burgundy -->
<section class="card card--burgundy">
  <div class="leaf leaf--top" role="img" aria-label="Decoración de hojas de agave"></div>
  <div class="leaf leaf--bottom" role="img" aria-label="Decoración de hojas de agave"></div>
  <div class="leaf leaf--left" role="img" aria-label="Decoración de hojas de agave"></div>
  <div class="leaf leaf--right" role="img" aria-label="Decoración de hojas de agave"></div>
  <svg class="frame" viewBox="0 0 504 288" fill="none" stroke="var(--line)" stroke-width="0.8">
    <path d="M217 18H36Q14 18 14 40V110"/><path d="M14 175V248Q14 270 36 270H218"/>
    <path d="M291 270H464Q486 270 486 248V175"/><path d="M486 101V40Q486 18 464 18H296"/>
    <g fill="var(--line)" stroke="none">
      <circle cx="217" cy="18" r="2"/><circle cx="296" cy="18" r="2"/>
      <circle cx="218" cy="270" r="2"/><circle cx="291" cy="270" r="2"/>
      <circle cx="14" cy="110" r="2"/><circle cx="14" cy="175" r="2"/>
      <circle cx="486" cy="101" r="2"/><circle cx="486" cy="175" r="2"/>
    </g>
  </svg>
  <div class="brand"><span class="brand__mark"></span><span class="brand__name">BELLWETHER</span></div>
  <h1 class="title">Restaurant Bellwether</h1>
  <ul class="contact">
    <li><svg viewBox="0 0 14 15"><path d="M2 2l3 0 1 3-2 1c1 2 2 3 4 4l1-2 3 1 0 3c-6 0-10-4-10-10z"/></svg>Reservaciones 958-555-0142</li>
    <li><svg viewBox="0 0 14 15"><path d="M7 14C3 9 2 7 2 5a5 5 0 0110 0c0 2-1 4-5 9z"/><circle cx="7" cy="5" r="1.8"/></svg>Jacarandá 415<br>Bahía del Sol,<br>Oaxaca CP 70900</li>
    <li><svg viewBox="0 0 14 15"><path d="M3 1v11l3-3 2 5 2-1-2-5h4z"/></svg>www.bellwether.com.mx</li>
  </ul>
</section>

<!-- Amber -->
<section class="card card--amber">
  <div class="leaf leaf--top" role="img" aria-label="Decoración de hojas de agave"></div>
  <div class="leaf leaf--bottom" role="img" aria-label="Decoración de hojas de agave"></div>
  <div class="leaf leaf--left" role="img" aria-label="Decoración de hojas de agave"></div>
  <div class="leaf leaf--right" role="img" aria-label="Decoración de hojas de agave"></div>
  <svg class="frame" viewBox="0 0 504 288" fill="none" stroke="var(--line)" stroke-width="0.8">
    <path d="M217 18H36Q14 18 14 40V110"/><path d="M14 175V248Q14 270 36 270H218"/>
    <path d="M291 270H464Q486 270 486 248V175"/><path d="M486 101V40Q486 18 464 18H296"/>
    <g fill="var(--line)" stroke="none">
      <circle cx="217" cy="18" r="2"/><circle cx="296" cy="18" r="2"/>
      <circle cx="218" cy="270" r="2"/><circle cx="291" cy="270" r="2"/>
      <circle cx="14" cy="110" r="2"/><circle cx="14" cy="175" r="2"/>
      <circle cx="486" cy="101" r="2"/><circle cx="486" cy="175" r="2"/>
    </g>
  </svg>
  <div class="brand"><span class="brand__mark"></span><span class="brand__name">BELLWETHER</span></div>
  <h1 class="title">Restaurant Bellwether</h1>
  <ul class="contact">
    <li><svg viewBox="0 0 14 15"><path d="M2 2l3 0 1 3-2 1c1 2 2 3 4 4l1-2 3 1 0 3c-6 0-10-4-10-10z"/></svg>Reservaciones 958-555-0142</li>
    <li><svg viewBox="0 0 14 15"><path d="M7 14C3 9 2 7 2 5a5 5 0 0110 0c0 2-1 4-5 9z"/><circle cx="7" cy="5" r="1.8"/></svg>Jacarandá 415<br>Bahía del Sol,<br>Oaxaca CP 70900</li>
    <li><svg viewBox="0 0 14 15"><path d="M3 1v11l3-3 2 5 2-1-2-5h4z"/></svg>www.bellwether.com.mx</li>
  </ul>
</section>

</body>
</html>
```